RiverKite Blister Pack Graphic

Design a print quality graphic foe insertion in blister packaging
based on the attached design Must be print ready
Template attached
Two sided print ...identical on both sides
DO NOT INCLUDE'54,000 hr 10 yr guarantee" from sample
DO NOT INCLUDE "free candlesleeve" from attached sample

Create new graphic for single bulb blister pack based previous on bulb and candlesleeve pack

Target Market(s)

RiverKite end users

Industry/Entity Type

Lighting Fixture

Font styles to use
Sans Serif

Colors
faa54b

Requirements
Must have
• Immediate eye appeal

```html
<!DOCTYPE html>
<html lang="en">
<head>
<meta charset="utf-8">
<title>RiverKite Blister Pack Insert</title>
<link rel="stylesheet" href="https://fonts.googleapis.com/css2?family=Roboto:wght@400;500;700&display=swap">
<style>
  :root {
    --page: #ffffff;
    --card: #0d0a0b;
    --frame: #f7d50a;
    --yellow: #f7d50a;
    --orange: #f0552a;
    --ember: #faa54b;
    --deep-red: #6e1420;
    --badge-red: #c8172b;
    --white: #ffffff;
    --ink: #141010;
  }
  * { margin: 0; padding: 0; box-sizing: border-box; }
  html, body { width: 1200px; height: 1200px; overflow: hidden; background: var(--page); }
  .canvas { position: relative; width: 1200px; height: 1200px; font-family: "Roboto", Arial, sans-serif; }

  .insert-card {
    position: absolute; left: 386px; top: 197px; width: 421px; height: 799px;
    background: var(--card);
  }
  .insert-frame {
    position: absolute; left: 21px; top: 21px; width: 377px; height: 757px;
    border: 6px solid var(--frame); overflow: hidden;
    background: linear-gradient(180deg, var(--card) 0%, var(--card) 28%, #2a0d10 42%, var(--deep-red) 62%, #8a1c1e 100%);
  }
  .wave-bands { position: absolute; left: 0; top: 0; width: 365px; height: 745px; }
  .brand-name {
    position: absolute; left: 0; right: 0; top: 88px; text-align: center;
    font-size: 38px; font-weight: 400; color: var(--orange); letter-spacing: 0.5px; line-height: 1;
  }
  .tagline {
    position: absolute; left: 0; right: 0; top: 208px; text-align: center;
    font-size: 21px; font-weight: 700; color: var(--yellow); line-height: 1;
  }
  .voltage-badge {
    position: absolute; left: 244px; top: 254px; width: 104px; height: 104px; border-radius: 50%;
    background: radial-gradient(circle at 50% 50%, #ff3a3a 0%, var(--badge-red) 45%, #5a0a12 80%);
    box-shadow: 0 0 0 3px rgba(247, 213, 10, 0.55), 0 0 16px 4px rgba(250, 165, 75, 0.6);
    display: flex; align-items: center; justify-content: center;
    color: var(--white); font-size: 23px; font-weight: 500;
  }
  .flame-field {
    position: absolute; left: 0; right: 0; bottom: 0; height: 278px;
    background: linear-gradient(180deg, rgba(240, 85, 42, 0) 0%, rgba(240, 85, 42, 0.55) 35%, var(--ember) 70%, var(--yellow) 100%);
  }
  .bulb-visual {
    position: absolute; left: 103px; top: 245px; width: 161px; height: 428px;
    border-radius: 50% 50% 40% 40% / 60% 60% 25% 25%;
    background: linear-gradient(180deg, #ffffff 0%, #f6f2ee 70%, #d9d4cf 100%);
  }
  .web-address {
    position: absolute; left: 0; right: 0; top: 727px; text-align: center;
    font-size: 15px; font-weight: 700; color: var(--ink); letter-spacing: 1px; line-height: 1;
  }
</style>
</head>
<body>
<div class="canvas">
  <div class="insert-card">
    <div class="insert-frame">
      <div class="flame-field" role="img" aria-label="Illustration of rising orange and yellow flames"></div>
      <svg class="wave-bands" viewBox="352 191 312 636" aria-hidden="true">
        <path d="M352,338 C420,342 470,345 520,342 C590,338 640,350 664,400 L664,432 C640,372 590,354 520,356 C460,358 400,356 352,356 Z" fill="var(--orange)"/>
        <path d="M352,300 C420,300 460,330 520,325 C580,320 630,302 664,298 L664,342 C620,334 580,340 520,344 C460,348 400,340 352,338 Z" fill="var(--yellow)"/>
      </svg>
      <div class="brand-name">RiverKite</div>
      <div class="tagline">World's Best Flame Bulb</div>
      <div class="voltage-badge">120V</div>
      <div class="bulb-visual" role="img" aria-label="Drawing of a white candle-shaped flame bulb with screw base"></div>
      <div class="web-address">www.riverkite.com</div>
    </div>
  </div>
</div>
</body>
</html>
```